Central Florida Lawn and Landscape business needs an awesome flyer design!

We are a growing lawn and landscape maintenance business looking to incorporate print mail for target advertising. This project should provide some editing capabilities for us to incorporate our logo, update any promotional offers, and adjust throughout the various seasons (lawn service, mulch jobs, one-time clean-ups, hardscape projects, etc). We'd like a clear call to action (one that we can edit if needed) to call or text today. We'll include our website address as well.
The business name is Velo Grassworks.
Target Market(s)
Residential homeowners
Industry/Entity Type
Lawn and landscape maintenance
Font styles to use
Other font styles liked:
- Couture
Look and feel

```html
<!DOCTYPE html>
<html lang="en">
<head>
<meta charset="utf-8">
<title>Velo Grassworks – Lawn & Landscape Flyer</title>
<link rel="stylesheet" href="https://fonts.googleapis.com/css2?family=Open+Sans:wght@400;600;700;800&display=swap">
<style>
:root{
  --green:#178b3f;
  --green-deep:#0f6a2e;
  --mint:#daecc4;
  --mint-soft:#c9e3ad;
  --ink:#1d1f1c;
  --white:#ffffff;
  --page:#eef0ed;
}
*{box-sizing:border-box;margin:0;padding:0}
html,body{width:1200px;height:2550px;overflow:hidden;background:var(--page);font-family:"Open Sans",sans-serif}
.flyer{position:absolute;left:50px;top:484px;width:1100px;height:1582px;background:var(--white);overflow:hidden}
.hero{position:absolute;left:0;top:0;width:1100px;height:511px;background:var(--green)}
.hero svg{position:absolute;left:0;top:0}
.hero-title{position:absolute;left:28px;top:18px;color:var(--white);font-weight:700;font-size:124px;line-height:105px;letter-spacing:-3px}
.brand{position:absolute;display:flex;flex-direction:column;align-items:center;color:var(--white);font-family:"Open Sans",sans-serif;font-weight:700}
.brand .dot{border:4px solid var(--white);border-radius:50%}
.brand-hero{right:50px;top:44px;font-size:34px}
.brand-hero .dot{width:66px;height:66px;margin-bottom:12px}
.intro{position:absolute;left:0;top:511px;width:1100px;height:560px;background:var(--mint)}
.photo{position:absolute;left:34px;width:400px}
.photo-house{top:24px;height:266px;background:linear-gradient(160deg,#2f5e2a,#6d8f4a 45%,#3b5a3a 70%,#7a5f3c)}
.photo-yard{top:297px;height:242px;background:linear-gradient(170deg,#5f7a3a,#c9a760 30%,#4f8a2e 60%,#3c7a24)}
.intro-copy{position:absolute;left:463px;top:42px;width:600px;color:var(--ink)}
.intro-heading{color:var(--green);font-weight:600;font-size:35px;line-height:44px}
.intro-lead{margin-top:12px;font-weight:700;font-size:18px;line-height:24px;text-transform:uppercase}
.intro-body{margin-top:28px;font-size:20.5px;line-height:26.5px}
.features{position:absolute;left:463px;top:446px;width:610px;height:92px}
.feature{position:absolute;top:0;width:180px;text-align:center;font-size:15px;text-transform:uppercase;color:var(--ink)}
.feature svg{display:block;margin:0 auto 8px}
.divider{position:absolute;top:6px;height:80px;border-left:4px dotted var(--green)}
.bottom{position:absolute;left:0;top:1071px;width:1100px;height:511px;background:var(--green);color:var(--white)}
.bottom svg.curve{position:absolute;left:0;top:0}
.section-title{position:absolute;font-weight:600;font-size:38px;line-height:46px}
.services{position:absolute;left:38px;top:112px;width:360px;list-style:none}
.services li{position:absolute;left:0;padding-left:34px}
.services h3{font-size:17.5px;font-weight:700;text-transform:uppercase;line-height:22px}
.services p{font-size:15px;line-height:19px;width:230px}
.tick{position:absolute;left:0;top:3px}
.reasons{position:absolute;left:448px;top:106px;list-style:none}
.reasons li{position:relative;padding-left:34px;height:39px;font-size:18px;font-weight:600}
.reasons li span{display:inline-block;border-bottom:2px dotted rgba(255,255,255,.55);padding-bottom:5px}
.brand-foot{left:856px;top:76px;font-size:34px}
.brand-foot .dot{width:70px;height:70px;margin-bottom:12px}
.contact{position:absolute;left:462px;top:300px;width:420px;height:176px;list-style:none}
.contact::before{content:"";position:absolute;left:39px;top:0;bottom:0;border-left:2px solid var(--white)}
.contact li{position:absolute;left:0;display:flex;align-items:center;font-size:28px;font-weight:700}
.contact li svg{width:28px;margin-right:24px}
</style>
</head>
<body>
<main class="flyer">
  <header class="hero">
    <svg width="1100" height="511" viewBox="0 0 1100 511">
      <defs>
        <linearGradient id="forest" x1="0" y1="0" x2="1" y2="1">
          <stop offset="0" stop-color="#5e7f35"/>
          <stop offset=".35" stop-color="#2c5a22"/>
          <stop offset=".6" stop-color="#6b4a25"/>
          <stop offset="1" stop-color="#1d4216"/>
        </linearGradient>
      </defs>
      <path role="img" aria-label="Modern glass house among lush forest garden with steps and flowering shrubs" d="M420,0 L1100,0 L1100,511 L336,511 C430,430 478,320 472,210 C466,120 448,55 420,0 Z" fill="url(#forest)"/>
    </svg>
    <h1 class="hero-title">Lawn &amp;<br>Landscape<br>Maintenance<br>Services</h1>
    <div class="brand brand-hero"><span class="dot"></span>Velo Grassworks</div>
  </header>

  <section class="intro">
    <div class="photo photo-house" role="img" aria-label="Contemporary home with wooden boardwalk over a garden pond"></div>
    <div class="photo photo-yard" role="img" aria-label="Green front yard with large oak tree, flower beds and a dog"></div>
    <div class="intro-copy">
      <h2 class="intro-heading">Love your Lawn and Landscapes</h2>
      <p class="intro-lead">Looking for reliable, professional lawn and<br>landscape care? We’ve got you covered year-round!</p>
      <p class="intro-body">WE do it by combining industry expertise with top-quality equipment and personalized service. Whether it’s routine lawn care, detailed landscaping, or specialized hardscaping, our experienced team ensures your outdoor spaces thrive. Each project is handled with precision, from assessing your lawn’s unique needs to executing efficient, professional care. By adapting to seasonal changes and customer preferences, we deliver consistent results that keep your yard looking its best year-round.</p>
    </div>
    <div class="features">
      <div class="feature" style="left:-20px">
        <svg width="48" height="48" viewBox="0 0 48 48" fill="none" stroke="#178b3f" stroke-width="2.5"><circle cx="24" cy="24" r="20"/><path d="M29 17c-1-2-3-3-5-3-3 0-5 2-5 4s2 3 5 4 5 2 5 4-2 4-5 4c-3 0-5-1-6-3M24 10v4M24 34v4"/></svg>
        Cost Effective
      </div>
      <div class="divider" style="left:195px"></div>
      <div class="feature" style="left:224px">
        <svg width="48" height="48" viewBox="0 0 48 48" fill="none" stroke="#178b3f" stroke-width="2.5"><path d="M8 30a16 16 0 0 1 32 0z"/><path d="M6 30h36v5H6zM20 14v10M28 14v10M15 42c2-4 5-6 9-6s7 2 9 6"/></svg>
        Latest Equipment
      </div>
      <div class="divider" style="left:419px"></div>
      <div class="feature" style="left:425px">
        <svg width="52" height="48" viewBox="0 0 52 48" fill="none" stroke="#178b3f" stroke-width="2.5"><circle cx="15" cy="11" r="5"/><path d="M7 44V24a8 8 0 0 1 16 0v20M15 30v14"/><circle cx="33" cy="13" r="5"/><path d="M26 44V26a7 7 0 0 1 14 0v18"/><path d="M40 8l4 4 7-8"/></svg>
        Skilled Labour
      </div>
    </div>
  </section>

  <section class="bottom">
    <svg class="curve" width="1100" height="511" viewBox="0 0 1100 511"><path d="M847,511 C900,385 995,300 1100,294 L1100,511 Z" fill="#daecc4"/></svg>

    <h2 class="section-title" style="left:38px;top:38px">Our Services</h2>
    <ul class="services">
      <li style="top:0"><svg class="tick" width="18" height="18" viewBox="0 0 18 18" fill="none" stroke="#c9e3ad" stroke-width="2"><circle cx="9" cy="9" r="7.5"/><path d="M5.5 9.5l2.5 2.5 5-5.5"/></svg><h3>Lawn Service:</h3><p>Keep your lawn looking fresh and green with our regular maintenance.</p></li>
      <li style="top:102px"><svg class="tick" width="18" height="18" viewBox="0 0 18 18" fill="none" stroke="#c9e3ad" stroke-width="2"><circle cx="9" cy="9" r="7.5"/><path d="M5.5 9.5l2.5 2.5 5-5.5"/></svg><h3>Mulch Jobs:</h3><p>Enhance your curb<br>appeal with high-quality mulch installation.</p></li>
      <li style="top:204px"><svg class="tick" width="18" height="18" viewBox="0 0 18 18" fill="none" stroke="#c9e3ad" stroke-width="2"><circle cx="9" cy="9" r="7.5"/><path d="M5.5 9.5l2.5 2.5 5-5.5"/></svg><h3>One-Time Clean-Ups:</h3><p>Tidy up your yard with our hassle-free clean-up services.</p></li>
      <li style="top:288px"><svg class="tick" width="18" height="18" viewBox="0 0 18 18" fill="none" stroke="#c9e3ad" stroke-width="2"><circle cx="9" cy="9" r="7.5"/><path d="M5.5 9.5l2.5 2.5 5-5.5"/></svg><h3>Hardscape Projects:</h3><p>Transform your outdoor space with beautiful patios, walkways, and more.</p></li>
    </ul>

    <h2 class="section-title" style="left:448px;top:38px">Why Choose Us</h2>
    <ul class="reasons">
      <li><svg class="tick" width="18" height="18" viewBox="0 0 18 18" fill="none" stroke="#c9e3ad" stroke-width="2"><circle cx="9" cy="9" r="7.5"/><path d="M5.5 9.5l2.5 2.5 5-5.5"/></svg><span>Locally owned and operated</span></li>
      <li><svg class="tick" width="18" height="18" viewBox="0 0 18 18" fill="none" stroke="#c9e3ad" stroke-width="2"><circle cx="9" cy="9" r="7.5"/><path d="M5.5 9.5l2.5 2.5 5-5.5"/></svg><span>Affordable, competitive rates</span></li>
      <li><svg class="tick" width="18" height="18" viewBox="0 0 18 18" fill="none" stroke="#c9e3ad" stroke-width="2"><circle cx="9" cy="9" r="7.5"/><path d="M5.5 9.5l2.5 2.5 5-5.5"/></svg><span>Reliable, on-time service</span></li>
      <li><svg class="tick" width="18" height="18" viewBox="0 0 18 18" fill="none" stroke="#c9e3ad" stroke-width="2"><circle cx="9" cy="9" r="7.5"/><path d="M5.5 9.5l2.5 2.5 5-5.5"/></svg><span>Customized care for every season</span></li>
    </ul>

    <div class="brand brand-foot"><span class="dot"></span>Velo Grassworks</div>

    <ul class="contact">
      <li style="top:8px"><svg viewBox="0 0 28 28" height="28" fill="none" stroke="#fff" stroke-width="2"><circle cx="14" cy="14" r="12"/><path d="M2 14h24M14 2c-4 4-5 8-5 12s1 8 5 12M14 2c4 4 5 8 5 12s-1 8-5 12"/></svg>www.velograssworks.com</li>
      <li style="top:63px"><svg viewBox="0 0 28 28" height="28" fill="none" stroke="#fff" stroke-width="2"><rect x="2" y="6" width="24" height="16"/><path d="M2 6l12 9 12-9"/></svg>info@velograssworks.com</li>
      <li style="top:122px"><svg viewBox="0 0 28 28" height="28" fill="none" stroke="#fff" stroke-width="2"><path d="M7 3l5 6-3 3c2 4 4 6 8 8l3-3 6 5-3 4C13 26 2 15 3 6z"/></svg>407-555-0183</li>
    </ul>
  </section>
</main>
</body>
</html>
```